Business cards / Letterheads / Compliment slips

We are looking to get business cards, letterheads and compliment slips designed.

These will all have to follow the design of our new website and logo. Links to the website, logo and fonts can be found below...

The designs need to be simple with focus on the typography. Only the following colours should be used on the designs...

#7f9d3c
#191818
#fff

Website:
http://brightfieldweb.samplework.co.uk/

Logo:
https://www.filecrate.example/sh/9xk2mwq7tvbalp4/qrtuPL8NzK/logos

Fonts:
https://www.filecrate.example/sh/9xk2mwq7tvbalp4/Hw7ZpRt3sQ/Fonts/BayerModern_TTF

and

https://www.filecrate.example/sh/9xk2mwq7tvbalp4/T6nVyo4Dc1/Fonts/MuseoSansFamily

Reason: We would like some more design submissions

Reason: We are still deciding on designs we like and would like to see some more submissions...

Industry/Entity Type

Business

Requirements
Must have
• The designs need to be simple with focus on the typography. Only the following colours should be used on the designs...

#7f9d3c
#191818
#fff
Should not have
• - Any fonts that are not provided.
- Any colours that are not provided.

```html
<!DOCTYPE html>
<html lang="en">
<head>
<meta charset="utf-8">
<title>Brightfield Stationery Set</title>
<link href="https://fonts.googleapis.com/css2?family=Mulish:wght@400;500;600;700&display=swap" rel="stylesheet">
<style>
  :root {
    --green: #7f9d3c;
    --ink: #191818;
    --paper: #ffffff;
    --slate: #4d4d4d;
    --stage: #ffffff;
    --text: #3a3a3a;
  }
  * { box-sizing: border-box; margin: 0; padding: 0; }
  html, body { width: 1200px; height: 1000px; overflow: hidden; background: var(--stage); }
  body { font-family: "Mulish", sans-serif; color: var(--text); position: relative; }
  .sheet { position: absolute; background: var(--paper); outline: 1px solid #e6e6e6; overflow: hidden; }
  .pattern-band {
    position: absolute; left: 0; right: 0;
    background: linear-gradient(90deg, var(--slate), #5b6a3c 50%, var(--slate));
  }
  .brand { position: absolute; display: flex; align-items: center; gap: 6px; }
  .brand-dot { border-radius: 50%; background: var(--green); flex: none; }
  .brand-name { font-weight: 600; color: var(--green); letter-spacing: -0.02em; line-height: 1; }
  .contact-list { position: absolute; list-style: none; }
  .contact-list li { display: flex; align-items: center; gap: 5px; }
  .icon { flex: none; }
  .icon circle { fill: var(--green); }
  .icon path { fill: none; stroke: var(--paper); stroke-width: 1.6; stroke-linecap: round; stroke-linejoin: round; }

  /* Letterhead */
  .letterhead { left: 65px; top: 157px; width: 468px; height: 665px; }
  .letterhead .pattern-band { height: 16px; }
  .letterhead .band-top { top: 0; }
  .letterhead .band-bottom { bottom: 0; }
  .letterhead .brand { left: 37px; top: 46px; }
  .letterhead .brand-dot { width: 28px; height: 28px; }
  .letterhead .brand-name { font-size: 23px; }
  .letterhead .contact-list { left: 300px; top: 41px; font-size: 7.5px; color: var(--ink); }
  .letterhead .contact-list li { margin-bottom: 5px; }
  .letter-body { position: absolute; left: 37px; top: 170px; width: 398px; font-size: 9.6px; line-height: 14.4px; color: var(--text); }
  .salutation { color: var(--green); font-size: 11.5px; margin-bottom: 2px; }
  .letter-body p { margin-bottom: 14px; text-align: justify; }
  .sign-off { position: absolute; left: 345px; top: 476px; font-size: 9.6px; line-height: 14px; }
  .signature { position: absolute; left: 323px; top: 496px; width: 90px; height: 48px; background: linear-gradient(90deg, #f2f2f2, #e4e4e4, #f2f2f2); border-radius: 4px; }
  .signatory { position: absolute; left: 345px; top: 566px; font-size: 9.6px; line-height: 14.5px; color: var(--ink); }

  /* Compliment slip */
  .comp-slip { left: 627px; top: 157px; width: 526px; height: 252px; }
  .comp-slip .pattern-band { height: 20px; }
  .comp-slip .band-top { top: 0; }
  .comp-slip .band-bottom { bottom: 0; }
  .comp-slip .brand { left: 8px; top: 42px; }
  .comp-slip .brand-dot { width: 30px; height: 30px; }
  .comp-slip .brand-name { font-size: 23px; }
  .slip-title { position: absolute; left: 0; right: 0; top: 88px; text-align: center; color: var(--green); font-size: 14px; font-weight: 600; letter-spacing: 0.02em; }
  .slip-copy { position: absolute; left: 25px; width: 488px; top: 112px; font-size: 11.6px; line-height: 14.6px; color: var(--text); text-align: justify; }
  .slip-contacts { position: absolute; left: 34px; right: 18px; top: 213px; display: flex; justify-content: space-between; font-size: 10px; color: var(--ink); }
  .slip-contacts span { display: flex; align-items: center; gap: 6px; }

  /* Business cards */
  .card { position: absolute; width: 212px; height: 121px; overflow: hidden; background: var(--paper); outline: 1px solid #e6e6e6; }
  .card-front-a { left: 667px; top: 490px; }
  .card-front-b { left: 945px; top: 643px; }
  .card-back-a { left: 945px; top: 490px; }
  .card-back-b { left: 667px; top: 643px; }
  .card-back { background: linear-gradient(135deg, var(--slate), #5b6a3c 50%, var(--slate)); }
  .card .brand { left: 9px; top: 47px; gap: 4px; }
  .card .brand-dot { width: 16px; height: 16px; }
  .card .brand-name { font-size: 14px; }
  .card-url { position: absolute; left: 13px; top: 71px; font-size: 4.8px; color: var(--ink); }
  .card-panel { position: absolute; left: 118px; top: 0; right: 0; bottom: 0; background: var(--slate); }
  .card-accent { position: absolute; left: 114px; top: 30px; width: 4px; height: 46px; background: var(--green); }
  .card .contact-list { left: 124px; top: 31px; font-size: 5px; line-height: 5.6px; color: var(--paper); }
  .card .contact-list li { margin-bottom: 4px; gap: 3px; }
</style>
</head>
<body>

<svg width="0" height="0" style="position:absolute" aria-hidden="true">
  <defs>
    <symbol id="icon-pin" viewBox="0 0 20 20"><circle cx="10" cy="10" r="10"/><path d="M10 15.5c-2.5-3-4-5-4-7a4 4 0 0 1 8 0c0 2-1.5 4-4 7z"/></symbol>
    <symbol id="icon-phone" viewBox="0 0 20 20"><circle cx="10" cy="10" r="10"/><path d="M7 5.5l2 2.5-1.2 1.5c.8 1.5 1.7 2.4 3 3l1.5-1.2 2.5 2-1.3 1.6c-3.5-.5-6.9-3.9-7.6-7.5z"/></symbol>
    <symbol id="icon-mail" viewBox="0 0 20 20"><circle cx="10" cy="10" r="10"/><path d="M5.5 6.5h9v7h-9zM5.5 6.5l4.5 4 4.5-4"/></symbol>
    <symbol id="icon-web" viewBox="0 0 20 20"><circle cx="10" cy="10" r="10"/><path d="M10 4.5a5.5 5.5 0 1 0 0 11a5.5 5.5 0 1 0 0-11M4.5 10h11M10 4.5c-2.2 3-2.2 8 0 11M10 4.5c2.2 3 2.2 8 0 11"/></symbol>
    <symbol id="icon-tag" viewBox="0 0 20 20"><circle cx="10" cy="10" r="10"/><path d="M8 5.5l-1 9M12.5 5.5l-1 9M5.5 8.5h9M5 12h9"/></symbol>
    <symbol id="icon-profile" viewBox="0 0 20 20"><circle cx="10" cy="10" r="10"/><path d="M10 6a2 2 0 1 0 0 4a2 2 0 1 0 0-4M6.5 14.5c.5-2 2-3 3.5-3s3 1 3.5 3"/></symbol>
  </defs>
</svg>

<!-- Letterhead -->
<section class="sheet letterhead">
  <div class="pattern-band band-top" role="img" aria-label="Repeating green circle pattern band"></div>
  <div class="brand"><span class="brand-dot"></span><span class="brand-name">brightfield</span></div>
  <ul class="contact-list">
    <li><svg class="icon" width="9" height="9"><use href="#icon-pin"/></svg><span>Floor 2, 24 Mill Lane<br>Harbourton, HB4 2QE</span></li>
    <li><svg class="icon" width="9" height="9"><use href="#icon-phone"/></svg><span>0845 310 4482</span></li>
    <li><svg class="icon" width="9" height="9"><use href="#icon-mail"/></svg><span>hello@brightfieldweb.co.uk</span></li>
    <li><svg class="icon" width="9" height="9"><use href="#icon-web"/></svg><span>http://brightfieldweb.samplework.co.uk/</span></li>
  </ul>
  <div class="letter-body">
    <div class="salutation">Dear Client</div>
    <p>This is a sample letter that has been placed to demonstrate the typing format on the (Your Company). letterhead design. When positioned properly, it will serve to work in harmony with all of the other elements on the letterhead.</p>
    <p>This letterhead design is meant to project an image of professionalism and reliability. By using simple alignments we have created a very spacious feeling. The simplicity suggests strength and the spaciousness contributes to the aesthetics of the layout. These basic qualities along with the (Your Company) colours, are consistent with the overall look and helps to reinforce the (Your Company) brand. This letterhead design is meant to project an image of professionalism and reliability. By using simple alignments we have created a very spacious feeling. The simplicity suggests strength and the spaciousness contributes to the aesthetics of the layout. These basic qualities along with the (Your Company) colours, are consistent with the overall look and helps to reinforce the (Your Company) brand.</p>
    <p>This letterhead design is based on the (Form of your logo) form the (Your Company) logo. Each stationery has a part of the (Form of your logo). Together, they form a perfect (Form of your logo) which become a strong design element of the (Your Company) brand).</p>
  </div>
  <div class="sign-off">Thank You</div>
  <div class="signature" role="img" aria-label="Handwritten signature"></div>
  <div class="signatory">Mr. Tom Harlow<br>Manager</div>
  <div class="pattern-band band-bottom" role="img" aria-label="Repeating green circle pattern band"></div>
</section>

<!-- Compliment slip -->
<section class="sheet comp-slip">
  <div class="pattern-band band-top" role="img" aria-label="Repeating green circle pattern band"></div>
  <div class="brand"><span class="brand-dot"></span><span class="brand-name">brightfield</span></div>
  <h2 class="slip-title">ABOUT BRIGHTFIELD</h2>
  <p class="slip-copy">"Lorem ipsum dolor sit amet, consectetur adipisicing elit, sed do eiusmod tempor incididunt ut labore et dolore magna aliqua. Ut enim ad minim veniam, quis nostrud exercitation ullamco laboris nisi ut aliquip ex ea commodo consequat. Duis aute irure dolor in reprehenderit in voluptate velit esse cillum dolore eu fugiat nulla pariatur. Excepteur sint occaecat cupidatat non proident, sunt in culpa qui officia deserunt mollit anim id est laborum."</p>
  <div class="slip-contacts">
    <span><svg class="icon" width="12" height="12"><use href="#icon-phone"/></svg>0845 310 4482</span>
    <span><svg class="icon" width="12" height="12"><use href="#icon-mail"/></svg>hello@brightfieldweb.co.uk</span>
    <span><svg class="icon" width="12" height="12"><use href="#icon-web"/></svg>http://brightfieldweb.samplework.co.uk/</span>
  </div>
  <div class="pattern-band band-bottom" role="img" aria-label="Repeating green circle pattern band"></div>
</section>

<!-- Business card fronts -->
<section class="card card-front-a">
  <div class="brand"><span class="brand-dot"></span><span class="brand-name">brightfield</span></div>
  <div class="card-url">http://brightfieldweb.samplework.co.uk/</div>
  <div class="card-panel"></div>
  <div class="card-accent"></div>
  <ul class="contact-list">
    <li><svg class="icon" width="6" height="6"><use href="#icon-pin"/></svg><span>Floor 2, 24 Mill Lane<br>Harbourton, HB4 2QE</span></li>
    <li><svg class="icon" width="6" height="6"><use href="#icon-phone"/></svg><span>0845 310 4482</span></li>
    <li><svg class="icon" width="6" height="6"><use href="#icon-mail"/></svg><span>hello@brightfieldweb.co.uk</span></li>
    <li><svg class="icon" width="6" height="6"><use href="#icon-tag"/></svg><span>@brightfield_web</span></li>
    <li><svg class="icon" width="6" height="6"><use href="#icon-profile"/></svg><span>Profile</span></li>
  </ul>
</section>

<section class="card card-front-b">
  <div class="brand"><span class="brand-dot"></span><span class="brand-name">brightfield</span></div>
  <div class="card-url">http://brightfieldweb.samplework.co.uk/</div>
  <div class="card-panel"></div>
  <div class="card-accent"></div>
  <ul class="contact-list">
    <li><svg class="icon" width="6" height="6"><use href="#icon-pin"/></svg><span>Floor 2, 24 Mill Lane<br>Harbourton, HB4 2QE</span></li>
    <li><svg class="icon" width="6" height="6"><use href="#icon-phone"/></svg><span>0845 310 4482</span></li>
    <li><svg class="icon" width="6" height="6"><use href="#icon-mail"/></svg><span>hello@brightfieldweb.co.uk</span></li>
    <li><svg class="icon" width="6" height="6"><use href="#icon-tag"/></svg><span>@brightfield_web</span></li>
    <li><svg class="icon" width="6" height="6"><use href="#icon-profile"/></svg><span>Profile</span></li>
  </ul>
</section>

<!-- Business card backs -->
<section class="card card-back card-back-a" role="img" aria-label="Card back with repeating green circle pattern"></section>
<section class="card card-back card-back-b" role="img" aria-label="Card back with repeating green circle pattern"></section>

</body>
</html>
```